Letterhead, stationery and email signature for construction business

I need the letterhead, stationery and email signature designs for a construction business. I want them to have a corporate feel to them.

I've attached the logo for reference.

```html
<!DOCTYPE html>
<html lang="en">
<head>
<meta charset="utf-8">
<title>Norvale Builders – Stationery</title>
<link rel="stylesheet" href="https://fonts.googleapis.com/css2?family=Archivo:wght@700&family=Roboto:wght@400;700&display=swap">
<style>
:root{
  --blue:#2d58a8;
  --slate:#4a4b57;
  --ink:#3a3b44;
  --paper:#ffffff;
  --faint:#f1f2f4;
  --header-bg:#d6d7db;
  --scene-bg:#2f3136;
  --desk-bg:#d0d1d5;
}
*{margin:0;padding:0;box-sizing:border-box}
html,body{width:1200px;height:2464px;overflow:hidden}
body{position:relative;background:var(--desk-bg);font-family:"Roboto",Arial,sans-serif;color:var(--ink)}
.abs{position:absolute}
.band-header{left:0;top:0;width:1200px;height:152px;background:linear-gradient(#e4e5e8,var(--header-bg))}
.band-scene{left:0;top:152px;width:1200px;height:838px;background:var(--scene-bg)}

/* wordmark */
.wordmark{display:flex;align-items:center;gap:8px;color:var(--blue);font-family:"Archivo",Arial,sans-serif;font-weight:700;line-height:1}
.wordmark .chip{background:var(--blue)}
.wordmark .name{display:flex;flex-direction:column}
.wordmark .line2{letter-spacing:.34em}

.paper{background:var(--paper);box-shadow:0 6px 18px rgba(0,0,0,.18)}
.faint-square{background:var(--faint)}
.contact{list-style:none;font-size:9px;color:var(--ink)}
.contact li{display:flex;align-items:flex-start;gap:5px;margin-bottom:5px}
.contact svg{flex:none;width:10px;height:10px}
.person-name{color:var(--blue);font-weight:700}
.person-role{font-size:7px}
</style>
</head>
<body>
<svg width="0" height="0" style="position:absolute">
  <symbol id="ic-pin" viewBox="0 0 10 10"><rect width="10" height="10" rx="2" fill="#2d58a8"/><path d="M5 2a2 2 0 0 1 2 2c0 1.5-2 4-2 4S3 5.5 3 4a2 2 0 0 1 2-2z" fill="#fff"/></symbol>
  <symbol id="ic-phone" viewBox="0 0 10 10"><rect width="10" height="10" rx="2" fill="#2d58a8"/><path d="M3 2.5l1.2 0 .5 1.5-.8.6a4 4 0 0 0 1.6 1.6l.6-.8 1.5.5v1.2C5 7.5 2.5 5 3 2.5z" fill="#fff"/></symbol>
  <symbol id="ic-mail" viewBox="0 0 10 10"><rect width="10" height="10" rx="2" fill="#2d58a8"/><rect x="2.3" y="3" width="5.4" height="4" fill="#fff"/><path d="M2.3 3L5 5.2 7.7 3" stroke="#2d58a8" stroke-width=".7" fill="none"/></symbol>
  <symbol id="ic-web" viewBox="0 0 10 10"><rect width="10" height="10" rx="2" fill="#2d58a8"/><path d="M3 2.5l4.3 3-1.9.3 1 2-.8.4-1-2-1.6 1.2z" fill="#fff"/></symbol>
</svg>

<!-- header -->
<header class="abs band-header">
  <div class="abs wordmark" style="left:484px;top:48px">
    <span class="chip" style="width:50px;height:56px"></span>
    <span class="name"><span style="font-size:40px">NORVALE</span><span class="line2" style="font-size:14px;margin-top:4px">BUILDERS</span></span>
  </div>
</header>

<!-- business cards, flat -->
<section class="abs band-scene">
  <article class="abs paper card-front" style="left:110px;top:260px;width:460px;height:260px;display:flex">
    <div style="width:200px;height:100%;background:var(--slate);position:relative">
      <div class="abs" style="left:60px;top:0;width:140px;height:170px;background:var(--blue)"></div>
    </div>
    <div style="flex:1;display:flex;align-items:center;justify-content:center">
      <div class="wordmark"><span class="name"><span style="font-size:36px">NORVALE</span><span class="line2" style="font-size:13px;margin-top:5px">BUILDERS</span></span></div>
    </div>
  </article>
  <article class="abs paper card-back" style="left:630px;top:260px;width:460px;height:260px;overflow:hidden">
    <div class="abs faint-square" style="right:30px;top:120px;width:150px;height:140px"></div>
    <div class="abs wordmark" style="left:28px;top:24px">
      <span class="chip" style="width:24px;height:26px"></span>
      <span class="name"><span style="font-size:22px">NORVALE</span><span class="line2" style="font-size:8px;margin-top:3px">BUILDERS</span></span>
    </div>
    <ul class="abs contact" style="left:28px;top:110px;font-size:11px">
      <li><svg><use href="#ic-pin"/></svg><span>88 Harbor Row, Suite 4<br>Austin, TX 0000</span></li>
      <li><svg><use href="#ic-phone"/></svg>001-555-0142</li>
      <li><svg><use href="#ic-mail"/></svg>info@norvalebuilders.com</li>
      <li><svg><use href="#ic-web"/></svg>NorvaleBuilders.com</li>
    </ul>
    <div class="abs" style="right:28px;top:70px;text-align:right">
      <div class="person-name" style="font-size:20px">DANA MARSH</div>
      <div class="person-role" style="font-size:10px">Chief Executive Officer</div>
    </div>
  </article>
</section>

<!-- phone wallpaper -->
<section class="abs" style="left:80px;top:1156px;width:320px;height:430px;background:#eceded;overflow:hidden">
  <div class="abs wordmark" style="left:94px;top:42px"><span class="name" style="align-items:center"><span style="font-size:24px">NORVALE</span><span class="line2" style="font-size:10px;margin-top:3px">BUILDERS</span></span></div>
  <div class="abs" style="left:0;top:130px;width:320px;height:300px;background:var(--slate)"></div>
  <div class="abs" style="left:80px;top:130px;width:240px;height:300px;background:var(--blue)"></div>
</section>

<!-- letterhead -->
<article class="abs paper letterhead" style="left:484px;top:1030px;width:486px;height:688px;overflow:hidden">
  <div class="abs faint-square" style="right:20px;top:460px;width:182px;height:200px"></div>
  <div class="abs wordmark" style="left:20px;top:22px">
    <span class="chip" style="width:22px;height:26px"></span>
    <span class="name"><span style="font-size:19px">NORVALE</span><span class="line2" style="font-size:8px;margin-top:2px">BUILDERS</span></span>
  </div>
  <div class="abs contact" style="right:18px;top:26px;display:flex;gap:5px;text-align:right">
    <span>88 Harbor Row, Suite 4<br>Austin, TX 0000</span><svg width="10" height="10"><use href="#ic-pin"/></svg>
  </div>
  <ul class="abs contact" style="left:20px;top:630px">
    <li><svg><use href="#ic-phone"/></svg>001-555-0142</li>
    <li><svg><use href="#ic-mail"/></svg>info@norvalebuilders.com</li>
    <li><svg><use href="#ic-web"/></svg>NorvaleBuilders.com</li>
  </ul>
</article>

<!-- small cards on desk -->
<article class="abs paper" style="left:848px;top:1125px;width:236px;height:146px;overflow:hidden">
  <div class="abs faint-square" style="right:26px;top:50px;width:64px;height:80px"></div>
  <div class="abs wordmark" style="left:16px;top:16px;gap:5px">
    <span class="chip" style="width:16px;height:18px"></span>
    <span class="name"><span style="font-size:14px">NORVALE</span><span class="line2" style="font-size:6px;margin-top:2px">BUILDERS</span></span>
  </div>
  <div class="abs" style="right:14px;top:16px;text-align:right">
    <div class="person-name" style="font-size:10px">DANA MARSH</div>
    <div class="person-role" style="font-size:5px">Chief Executive Officer</div>
  </div>
  <ul class="abs contact" style="left:16px;top:78px;font-size:6px">
    <li><svg style="width:7px;height:7px"><use href="#ic-pin"/></svg><span>88 Harbor Row, Suite 4<br>Austin, TX 0000</span></li>
    <li><svg style="width:7px;height:7px"><use href="#ic-phone"/></svg>001-555-0142</li>
    <li><svg style="width:7px;height:7px"><use href="#ic-mail"/></svg>info@norvalebuilders.com</li>
    <li><svg style="width:7px;height:7px"><use href="#ic-web"/></svg>NorvaleBuilders.com</li>
  </ul>
</article>
<article class="abs paper" style="left:846px;top:1327px;width:242px;height:147px;display:flex">
  <div style="width:120px;background:var(--slate);position:relative"><div class="abs" style="left:36px;top:0;width:84px;height:100px;background:var(--blue)"></div></div>
  <div style="flex:1;display:flex;align-items:center;justify-content:center">
    <div class="wordmark"><span class="name" style="align-items:center"><span style="font-size:18px">NORVALE</span><span class="line2" style="font-size:7px;margin-top:2px">BUILDERS</span></span></div>
  </div>
</article>

<!-- email signature -->
<article class="abs paper email-signature" style="left:63px;top:1760px;width:624px;height:158px;overflow:hidden">
  <div class="abs faint-square" style="left:482px;top:18px;width:120px;height:126px"></div>
  <div class="abs wordmark" style="left:22px;top:16px">
    <span class="chip" style="width:26px;height:30px"></span>
    <span class="name"><span style="font-size:22px">NORVALE</span><span class="line2" style="font-size:9px;margin-top:2px">BUILDERS</span></span>
  </div>
  <div class="abs" style="left:22px;top:74px">
    <div class="person-name" style="font-size:17px">DANA MARSH</div>
    <div class="person-role" style="font-size:7px;margin-top:2px">Chief Executive Officer</div>
  </div>
  <ul class="abs contact" style="left:22px;top:110px">
    <li><svg><use href="#ic-phone"/></svg>001-555-0142</li>
    <li><svg><use href="#ic-mail"/></svg>info@norvalebuilders.com</li>
    <li><svg><use href="#ic-web"/></svg>NorvaleBuilders.com</li>
  </ul>
  <ul class="abs contact" style="left:162px;top:110px">
    <li><svg><use href="#ic-pin"/></svg><span>88 Harbor Row, Suite 4<br>Austin, TX 0000</span></li>
  </ul>
</article>

<!-- envelope -->
<article class="abs paper envelope" style="left:466px;top:1983px;width:672px;height:340px;overflow:hidden">
  <div class="abs faint-square" style="left:474px;top:118px;width:168px;height:190px"></div>
  <div class="abs wordmark" style="left:22px;top:22px">
    <span class="chip" style="width:26px;height:34px"></span>
    <span class="name"><span style="font-size:23px">NORVALE</span><span class="line2" style="font-size:9px;margin-top:2px">BUILDERS</span></span>
  </div>
  <div class="abs contact" style="left:22px;top:312px;display:flex;gap:5px">
    <svg width="10" height="10"><use href="#ic-pin"/></svg><span>88 Harbor Row, Suite 4 Austin, TX 0000</span>
  </div>
</article>
</body>
</html>
```